Business Card Design

Vintage looking Hair Salon, where the customer service is 100%. We are based in a cottage. With shabby chic console tables and beautiful ornate mirrors..and rich brown leather cutting chairs. Chandeliers at the window, and a ornate patchwork sofa.
our clientele are 28years upwards.. Mums with small children.. Ladies that lunch, and men that want more than a barbers and are prepared to pay for our services.
I am looking for a classy business card.. That look expensive.. Where our initials WHP become a visual reference.. I was thinking of cream card initials in black on a embossed tarnished silver.. But I'm open to suggestion. I want,  need the design to be able to work with flyers price list ect.

Willowmere Hair Parlour
27 Fenwick Row
Ardley Green
bN42 6TW
FB thewillowmerehairparlour
Info@thewillowmerhairparlour.co.uk
0208 715 2964

```html
<!DOCTYPE html>
<html lang="en">
<head>
<meta charset="UTF-8">
<title>Willowmere Hair Parlour — Business Card</title>
<link rel="stylesheet" href="https://fonts.googleapis.com/css2?family=Poiret+One&display=swap">
<style>
  :root {
    --backdrop: #8d8a86;
    --card-black: #1c1b1b;
    --card-sheen: #2e2c2b;
    --silver: #f2f0ec;
    --silver-soft: #cfcbc4;
    --placeholder-light: #6e6a66;
    --placeholder-dark: #3a3836;
  }
  * { margin: 0; padding: 0; box-sizing: border-box; }
  html, body {
    width: 1200px;
    height: 900px;
    overflow: hidden;
    background: var(--backdrop);
  }
  .business-card {
    position: absolute;
    left: 100px;
    top: 165px;
    width: 1000px;
    height: 570px;
    background: radial-gradient(ellipse at 50% 40%, var(--card-sheen) 0%, var(--card-black) 75%);
    font-family: "Poiret One", "Century Gothic", sans-serif;
    color: var(--silver);
  }
  .card-frame {
    position: absolute;
    inset: 0;
  }
  .corner-ornament {
    position: absolute;
    width: 54px;
    height: 54px;
    background: radial-gradient(circle at center, var(--placeholder-light), var(--placeholder-dark));
  }
  .corner-ornament.top-left { left: 32px; top: 32px; }
  .corner-ornament.top-right { right: 32px; top: 32px; }
  .corner-ornament.bottom-left { left: 32px; bottom: 32px; }
  .corner-ornament.bottom-right { right: 32px; bottom: 32px; }
  .mirror-emblem {
    position: absolute;
    left: 50%;
    top: 62px;
    width: 170px;
    height: 210px;
    margin-left: -85px;
    background: radial-gradient(ellipse at center, var(--placeholder-light), var(--placeholder-dark));
  }
  .chandelier {
    position: absolute;
    top: 120px;
    width: 62px;
    height: 62px;
    background: radial-gradient(circle at center, var(--placeholder-light), var(--placeholder-dark));
  }
  .chandelier.left { left: 250px; }
  .chandelier.right { right: 250px; }
  .salon-name {
    position: absolute;
    left: 0;
    right: 0;
    top: 300px;
    text-align: center;
    font-size: 58px;
    line-height: 70px;
    letter-spacing: 6px;
    text-transform: uppercase;
    font-weight: 400;
  }
  .contact-details {
    position: absolute;
    left: 0;
    right: 0;
    top: 380px;
    list-style: none;
    text-align: center;
    font-size: 21px;
    line-height: 30px;
    letter-spacing: 1.5px;
    color: var(--silver-soft);
  }
</style>
</head>
<body>
  <article class="business-card">
    <svg class="card-frame" width="1000" height="570" viewBox="0 0 1000 570" aria-hidden="true">
      <rect x="16" y="16" width="968" height="538" fill="none" stroke="#f2f0ec" stroke-width="4"/>
      <rect x="28" y="28" width="944" height="514" fill="none" stroke="#cfcbc4" stroke-width="1.2"/>
    </svg>

    <div class="corner-ornament top-left" role="img" aria-label="Filigree corner ornament"></div>
    <div class="corner-ornament top-right" role="img" aria-label="Filigree corner ornament"></div>
    <div class="corner-ornament bottom-left" role="img" aria-label="Filigree corner ornament"></div>
    <div class="corner-ornament bottom-right" role="img" aria-label="Filigree corner ornament"></div>

    <div class="chandelier left" role="img" aria-label="Small candle chandelier illustration"></div>
    <div class="mirror-emblem" role="img" aria-label="Ornate baroque mirror frame illustration with comb and scissors"></div>
    <div class="chandelier right" role="img" aria-label="Small candle chandelier illustration"></div>

    <h1 class="salon-name">Willowmere Hair Parlour</h1>

    <ul class="contact-details">
      <li>27 Fenwick Row · Ardley Green · bN42 6TW</li>
      <li>FB thewillowmerehairparlour</li>
      <li>Info@thewillowmerhairparlour.co.uk</li>
      <li>0208 715 2964</li>
    </ul>
  </article>
</body>
</html>
```